Company providing Business Management Services needs modern business card

The business provides services like tender preparation, bank submissions, business health checks, financial and admin support. We want to portray 'Trust', 'Strength' and 'Support'.
2 styles of logo in various formats have been uploaded.
Looking for easy to understand, yet sophisticated and stand out from the crowd.

Target Market(s)

Small and Medium sized businesses

Industry/Entity Type

Business

Contact Information for Business Card

Name - Daniel Vesterby, Description - Manager, Phone - 0472 915 603, Email - danielvesterby@kpwholdingsgroup.example, Work description - Business Management Services.

Requirements
Must have
• Logo

```html
<!DOCTYPE html>
<html lang="en">
<head>
<meta charset="utf-8">
<title>KPW Holdings Group — Business Card</title>
<link rel="stylesheet" href="https://fonts.googleapis.com/css2?family=Roboto+Condensed:wght@400&display=swap">
<style>
  :root {
    --page: #ffffff;
    --card: #040404;
    --text: #ffffff;
    --purple: #9b5199;
    --blue: #2c5ea8;
    --green: #4fab4a;
    --orange: #ee7623;
  }
  html, body {
    margin: 0;
    width: 1200px;
    height: 900px;
    overflow: hidden;
    background: var(--page);
    font-family: "Roboto Condensed", "Arial Narrow", sans-serif;
  }
  .card {
    position: absolute;
    left: 122px;
    top: 165px;
    width: 955px;
    height: 573px;
    background: var(--card);
    color: var(--text);
  }
  .identity {
    position: absolute;
    right: 80px;
    top: 72px;
    text-align: right;
  }
  .identity__name {
    font-size: 36px;
    line-height: 40px;
    margin: 0;
    font-weight: 400;
  }
  .identity__role {
    font-size: 20px;
    margin: 2px 0 0;
  }
  .contacts {
    position: absolute;
    left: 64px;
    top: 230px;
    list-style: none;
    margin: 0;
    padding: 0;
  }
  .contacts__item {
    display: flex;
    align-items: center;
    height: 22px;
    font-size: 20px;
    margin-bottom: 23.5px;
  }
  .contacts__icon {
    width: 22px;
    height: 22px;
    margin-right: 10px;
    fill: var(--text);
  }
  .brand {
    position: absolute;
    right: 80px;
    top: 255px;
    display: flex;
    align-items: center;
  }
  .brand__square {
    width: 96px;
    height: 96px;
    background: var(--text);
    margin-right: 26px;
  }
  .brand__name {
    font-size: 46px;
    line-height: 52px;
    text-align: right;
    color: var(--text);
  }
  .tagline {
    position: absolute;
    right: 92px;
    top: 415px;
    font-size: 21px;
  }
  .color-band {
    position: absolute;
    left: 0;
    bottom: 0;
    width: 100%;
    height: 38px;
    display: flex;
  }
  .color-band span { flex: 1; }
  .color-band .purple { background: var(--purple); }
  .color-band .blue { background: var(--blue); }
  .color-band .green { background: var(--green); }
  .color-band .orange { background: var(--orange); }
</style>
</head>
<body>
  <div class="card">
    <div class="identity">
      <h1 class="identity__name">Daniel Vesterby</h1>
      <p class="identity__role">Manager</p>
    </div>

    <ul class="contacts">
      <li class="contacts__item">
        <svg class="contacts__icon" viewBox="0 0 24 24" aria-hidden="true"><path d="M12 1a7 7 0 0 0-7 7c0 5.3 7 15 7 15s7-9.7 7-15a7 7 0 0 0-7-7zm0 9.6a2.6 2.6 0 1 1 0-5.2 2.6 2.6 0 0 1 0 5.2z"/></svg>
        415 Harbour Street, Brookfield 54321
      </li>
      <li class="contacts__item">
        <svg class="contacts__icon" viewBox="0 0 24 24" aria-hidden="true"><path d="M2 8c0-2 2-3 10-3s10 1 10 3v2h-5V8H7v2H2z"/><path d="M5 12h14l1 7H4z"/></svg>
        0472 915 603
      </li>
      <li class="contacts__item">
        <svg class="contacts__icon" viewBox="0 0 24 24" aria-hidden="true"><path d="M2 5h20v14H2z M4 7v.4l8 6 8-6V7z" fill-rule="evenodd"/></svg>
        danielvesterby@kpwholdingsgroup.example
      </li>
      <li class="contacts__item">
        <svg class="contacts__icon" viewBox="0 0 24 24" aria-hidden="true" fill="none" stroke="#fff" stroke-width="2.2" stroke-linecap="round"><path d="M10 14l4-4"/><path d="M8 12l-3 3a3 3 0 0 0 4 4l3-3"/><path d="M16 12l3-3a3 3 0 0 0-4-4l-3 3"/></svg>
        www.kpwholdings.example
      </li>
    </ul>

    <div class="brand">
      <div class="brand__square"></div>
      <div class="brand__name">KPW Holdings<br>Group</div>
    </div>

    <div class="tagline">Business Management Services</div>

    <div class="color-band">
      <span class="purple"></span><span class="blue"></span><span class="green"></span><span class="orange"></span>
    </div>
  </div>
</body>
</html>
```